Wayline Billboard Co Business Card Design

We have a newly created business and logo, but we now need business cards using the new logo.
We are an Australian based business, and we sell advertising space on trucks. The business cards will be seen by media buyers, direct advertisers, fleet owners and business people in general.
Our colours are very simple - black and a strong yellow, with some white. We have chosen the black and yellow for various reasons, but in particular because they are high contrast, and they also have a parallel with the number plates used on our roads, which is relevant to our product offering.
My initial thoughts:
Keep it simple and uncluttered
Use both sides
Our default is Century Gothic
I can provide logo files as required. We do not yet have a website, so I can't direct you there just yet. That may well be another project!
Target Market(s)
The business cards will be seen by media buyers, direct advertisers, fleet owners and business people in general.
Industry/Entity Type
Advertising
Look and feel
Each slider illustrates characteristics of the customer's brand and the style your logo design should communicate.

```html
<!DOCTYPE html>
<html lang="en">
<head>
<meta charset="UTF-8">
<title>Wayline Billboard Co – Business Card</title>
<link rel="stylesheet" href="https://fonts.googleapis.com/css2?family=Questrial&display=swap">
<style>
  :root {
    --brand-yellow: #f2e100;
    --brand-black: #0b0b0b;
    --card-white: #ffffff;
    --ink: #1a1a1a;
    --backdrop: #e9e7e3;
  }
  * { margin: 0; padding: 0; box-sizing: border-box; }
  html, body {
    width: 1200px;
    height: 900px;
    overflow: hidden;
    background: var(--backdrop);
    font-family: "Questrial", "Century Gothic", sans-serif;
  }
  .canvas {
    position: relative;
    width: 1200px;
    height: 900px;
    display: flex;
    flex-direction: column;
    align-items: center;
    justify-content: center;
    gap: 40px;
  }
  .card {
    position: relative;
    width: 620px;
    height: 380px;
    box-shadow: 0 10px 24px rgba(0,0,0,0.18);
  }

  /* Back side */
  .card-back {
    background: var(--brand-black);
    display: flex;
    align-items: center;
    justify-content: center;
  }
  .card-back .frame {
    position: absolute;
    inset: 26px;
    border: 16px solid var(--brand-yellow);
    border-radius: 36px;
  }
  .card-back .wordmark {
    position: relative;
    color: var(--brand-yellow);
    font-size: 34px;
    letter-spacing: 1px;
  }

  /* Front side */
  .card-front {
    background: var(--card-white);
    color: var(--ink);
    padding: 34px 44px 0;
  }
  .card-front .wordmark {
    text-align: center;
    color: var(--brand-yellow);
    font-size: 36px;
    letter-spacing: 1px;
    margin-top: 18px;
  }
  .card-front .website {
    text-align: center;
    font-size: 17px;
    margin-top: 8px;
  }
  .person {
    display: flex;
    align-items: baseline;
    justify-content: center;
    margin-top: 30px;
    padding-bottom: 6px;
    border-bottom: 1.5px solid var(--ink);
  }
  .person .name { font-size: 26px; }
  .person .role {
    font-size: 18px;
    border-left: 1px solid var(--ink);
    margin-left: 6px;
    padding-left: 6px;
  }
  .details {
    display: flex;
    justify-content: space-between;
    align-items: flex-start;
    margin-top: 22px;
  }
  .contacts { list-style: none; font-size: 17px; }
  .contacts li {
    display: flex;
    align-items: center;
    gap: 12px;
    line-height: 24px;
  }
  .contacts svg { width: 14px; height: 14px; fill: var(--brand-yellow); }
  .address {
    font-style: normal;
    font-size: 18px;
    line-height: 23px;
    margin-top: 26px;
  }
</style>
</head>
<body>
<main class="canvas">
  <section class="card card-back" aria-label="Card back">
    <div class="frame"></div>
    <div class="wordmark">Wayline Billboard Co</div>
  </section>

  <section class="card card-front" aria-label="Card front">
    <div class="wordmark">Wayline Billboard Co</div>
    <div class="website">WAYLINE.COM.AU</div>

    <div class="person">
      <span class="name">Dean Harlow</span>
      <span class="role">FOUNDER</span>
    </div>

    <div class="details">
      <ul class="contacts">
        <li>
          <svg viewBox="0 0 16 16" aria-hidden="true"><path d="M3 1l3 3-2 2c1 2 3 4 5 5l2-2 3 3-2 2C7 14 2 9 1 3z"/></svg>
          1800WAYLINE
        </li>
        <li>
          <svg viewBox="0 0 16 16" aria-hidden="true"><path d="M4 1h8v14H4z M5.5 3v8h5V3z"/></svg>
          +61 4 2850 3176
        </li>
        <li>
          <svg viewBox="0 0 16 16" aria-hidden="true"><path d="M1 3h14v10H1z M2 4l6 5 6-5z"/></svg>
          dean@wayline.com.au
        </li>
      </ul>
      <address class="address">
        Wayline Billboard Co<br>
        PO Box 2417<br>
        Harbour Point NSW 2095
      </address>
    </div>
  </section>
</main>
</body>
</html>
```